Tor'k Wayfarer Travel

We need a sleek, professional, inviting card to elicit global travel for the experienced and professional traveler. Royal blue, black and silver. (perhaps the wording could be silver with black shadow?-get creative) Maybe a watermark on the front and the full raised logo on the back.
We want a stylish and modern card, but professional.

```html
<!DOCTYPE html>
<html lang="en">
<head>
<meta charset="utf-8">
<title>Tor'k Wayfarer Travel — Business Card</title>
<link href="https://fonts.googleapis.com/css2?family=Open+Sans:wght@400;600;700;800&display=swap" rel="stylesheet">
<style>
  :root {
    --page-bg: #2a2a2c;
    --card-bg: #1c1c1e;
    --brand-blue: #29a8e0;
    --accent-green: #8dc63f;
    --text-grey: #d4d4d4;
    --silver: #8e8e90;
  }
  * { box-sizing: border-box; margin: 0; padding: 0; }
  html, body {
    width: 1200px; height: 900px; overflow: hidden;
    background: var(--page-bg);
    font-family: "Open Sans", Arial, sans-serif;
  }
  .sheet {
    width: 1200px; height: 900px;
    display: flex; flex-direction: column;
    align-items: center; justify-content: center; gap: 48px;
  }
  .card {
    position: relative;
    width: 700px; height: 400px;
    background: var(--card-bg);
    border-bottom: 7px solid var(--brand-blue);
    box-shadow: 0 12px 30px rgba(0,0,0,.45);
    overflow: hidden;
  }
  /* Front */
  .card-front { display: flex; align-items: center; }
  .brand-block {
    width: 345px; padding-left: 48px;
    display: flex; align-items: center; gap: 12px;
  }
  .brand-dot {
    width: 14px; height: 14px; border-radius: 50%;
    background: var(--brand-blue); flex: none;
  }
  .brand-name {
    color: var(--brand-blue);
    font-weight: 700; font-size: 26px; line-height: 1.2;
  }
  .divider {
    width: 1.5px; height: 190px; background: var(--brand-blue);
  }
  .contact-block { padding-left: 30px; color: var(--text-grey); }
  .person-name {
    color: var(--brand-blue); font-weight: 800;
    font-size: 24px; text-transform: uppercase; letter-spacing: .5px;
  }
  .person-title { font-size: 17px; margin-bottom: 14px; }
  .address { font-size: 17px; line-height: 1.35; margin-bottom: 12px; }
  .contact-list { list-style: none; font-size: 17px; line-height: 1.45; }
  .contact-list li { display: flex; align-items: center; gap: 9px; }
  .contact-list svg { width: 14px; height: 14px; flex: none; fill: var(--accent-green); }
  /* Back */
  .card-back { display: flex; align-items: center; justify-content: center; }
  .back-name {
    color: var(--silver); font-weight: 700; font-size: 46px;
  }
</style>
</head>
<body>
<main class="sheet">
  <section class="card card-front" aria-label="Card front">
    <div class="brand-block">
      <span class="brand-dot"></span>
      <span class="brand-name">Tor'k Wayfarer Travel</span>
    </div>
    <div class="divider"></div>
    <div class="contact-block">
      <p class="person-name">Dale Ferrano</p>
      <p class="person-title">President</p>
      <p class="address">1180 Marina Crest Way<br>Seacliff CA 92601</p>
      <ul class="contact-list">
        <li>
          <svg viewBox="0 0 16 16" aria-hidden="true"><path d="M3.5 1.5 6 1l1.5 3.5-1.8 1.2a8 8 0 0 0 4.6 4.6L11.5 8.5 15 10l-.5 2.5c-.2 1-1.2 1.8-2.3 1.6C6.6 13.3 2.7 9.4 1.9 3.8c-.2-1.1.6-2.1 1.6-2.3z"/></svg>
          555-014-2287
        </li>
        <li>
          <svg viewBox="0 0 16 16" aria-hidden="true"><path d="M1 3h14v10H1z M1.8 3.6 8 8.6l6.2-5H1.8z" fill-rule="evenodd"/></svg>
          info@torkwayfarer.com
        </li>
        <li>
          <svg viewBox="0 0 16 16" aria-hidden="true"><circle cx="8" cy="8" r="7"/><path d="M5 4c1.5 0 2 1.5 1 2.5S4 8 5.5 9.5 7 12 6 14M10 2.5c-.5 1.5.5 2.5 2 2.5s1.5 2 .5 3" stroke="#1c1c1e" stroke-width="1.2" fill="none"/></svg>
          www.torkwayfarer.com
        </li>
      </ul>
    </div>
  </section>

  <section class="card card-back" aria-label="Card back">
    <span class="back-name">Tor'k Wayfarer Travel</span>
  </section>
</main>
</body>
</html>
```